Circular Wedding Menu Design - Adobe Illustrator

I am looking for a design for circular wedding menus. these will be 7 inches.I'm providing a template from the printer, AI files of our wedding invitation, and the menu items.

The paper our invitations were printed on was a sandy beige color. please make the background for this the same color. It will be put ontop of a white plate with ivory tablecloth and cappucino covered napkins.

IMPORTANT - We aren't committed to a specific design so feel free to use whatever you like, but we definitely want the cow, fish, and carrot images from our rsvp to be used for the entrees in the menu.

IMPORTANT - must be in Adobe illustrator format

for inspiration:
http://cdn.velvorabridalnotes.example/wp-content/uploads/2012/10/tormane-styled-19.jpg

http://www.quorbelsearch.example/imgres?imgurl=http%3A%2F%2Fwww.dellivanestudio.example%2Fblog%2Fwp-content%2Fuploads%2F2013%2F07%2FPetal-Ledger-Round-Menu-Wedding-Place-Setting.jpg&imgrefurl=http%3A%2F%2Fwww.dellivanestudio.example%2Fblog%2Finspiration%2Fsimply-lovely-wedding-menu-place-settings%2F&h=815&w=600&tbnid=8kRqzp_4LUTWEN%3A&zoom=1&docid=72HJKs9PqMxaTN&ei=QwERtYu8LpMsoBF2xdDTRk&tbm=isch&ved=0DHtRNzhKNBk&iact=rc&uact=3&dur=526&page=1&start=0&ndsp=30

https://thumbs3.pixorvane.example/images?q=tbn:QWe7KpLmNvBxRtYu2Hs4DfGhJkZxCvBnMqWeRtYuIoPaSdFgHjK

https://thumbs3.pixorvane.example/images?q=tbn:ZxC8vBnMqW_e42RT_yUioPaSdFgHjKlZxCv66BnM7q_WERtyUiOp

https://thumbs2.pixorvane.example/images?q=tbn:LkJh5GfDsAp9OiUyTrEwQ-MNbV8cXzL3KjHgFdsaPoIuYtReW0Q

Industry/Entity Type

Wedding

```html
<!DOCTYPE html>
<html lang="en">
<head>
<meta charset="utf-8">
<title>Wedding Menu</title>
<link rel="stylesheet" href="https://fonts.googleapis.com/css2?family=Courgette&family=Great+Vibes&display=swap">
<style>
  :root {
    --rim-brown: #7b4f27;
    --band-tan: #bd8f5e;
    --line-cream: #f6e6d3;
    --paper: #fbeee3;
    --ribbon-face: #deb792;
    --ribbon-tail: #b98a5a;
    --ribbon-fold: #8a5a32;
    --ink: #141414;
    --leaf-grey: #a9a39c;
  }
  html, body {
    margin: 0;
    padding: 0;
    width: 1200px;
    height: 1200px;
    overflow: hidden;
    background: #ffffff;
  }
  .menu-card {
    position: relative;
    width: 1200px;
    height: 1200px;
  }
  .menu-card__frame {
    position: absolute;
    inset: 0;
  }
  .menu-card__text {
    position: absolute;
    left: 0;
    width: 1190px;
    text-align: center;
    color: var(--ink);
    font-family: "Courgette", cursive;
    margin: 0;
    white-space: nowrap;
  }
  .menu-title {
    top: 168px;
    font-family: "Great Vibes", cursive;
    font-size: 118px;
    line-height: 1;
    font-weight: 700;
    -webkit-text-stroke: 1.5px var(--ink);
  }
  .course-heading {
    font-size: 40px;
    line-height: 1;
  }
  .course-heading--cake { font-size: 41px; }
  .dish-line {
    font-size: 18.5px;
    line-height: 1;
  }
  .entree-icon {
    position: absolute;
  }
</style>
</head>
<body>
<main class="menu-card">
  <svg class="menu-card__frame" width="1200" height="1200" viewBox="0 0 1200 1200">
    <defs>
      <clipPath id="paper-clip"><circle cx="600" cy="600" r="503"/></clipPath>
      <radialGradient id="leaf-tone" cx="50%" cy="50%" r="50%">
        <stop offset="0%" stop-color="var(--leaf-grey)" stop-opacity="0.35"/>
        <stop offset="100%" stop-color="var(--leaf-grey)" stop-opacity="0"/>
      </radialGradient>
    </defs>

    <!-- rim and bands -->
    <circle cx="600" cy="600" r="600" fill="var(--rim-brown)"/>
    <circle cx="600" cy="600" r="536" fill="var(--band-tan)"/>
    <circle cx="600" cy="600" r="527" fill="none" stroke="var(--line-cream)" stroke-width="3"/>
    <circle cx="600" cy="600" r="516" fill="none" stroke="var(--line-cream)" stroke-width="5"/>
    <circle cx="600" cy="600" r="503" fill="var(--paper)"/>

    <!-- foliage areas -->
    <g clip-path="url(#paper-clip)">
      <ellipse role="img" aria-label="Leafy branch sketch" cx="230" cy="450" rx="150" ry="100" fill="url(#leaf-tone)"/>
      <ellipse role="img" aria-label="Small leaf sprig" cx="160" cy="630" rx="60" ry="50" fill="url(#leaf-tone)"/>
      <ellipse role="img" aria-label="Leafy branches climbing the right edge" cx="960" cy="560" rx="190" ry="380" fill="url(#leaf-tone)"/>
      <ellipse role="img" aria-label="Leaf sprigs along the bottom edge" cx="570" cy="1040" rx="170" ry="60" fill="url(#leaf-tone)"/>
    </g>

    <!-- ribbon banner -->
    <g class="menu-ribbon">
      <polygon points="327,246 492,246 492,342 327,342 366,294" fill="var(--ribbon-tail)"/>
      <polygon points="873,246 708,246 708,342 873,342 834,294" fill="var(--ribbon-tail)"/>
      <polygon points="400,288 492,288 492,318" fill="var(--ribbon-fold)"/>
      <polygon points="800,288 708,288 708,318" fill="var(--ribbon-fold)"/>
      <path d="M384 210 Q594 180 800 210 L800 288 Q594 258 384 288 Z" fill="var(--ribbon-face)"/>
    </g>
  </svg>

  <h1 class="menu-card__text menu-title">Menu</h1>

  <h2 class="menu-card__text course-heading" style="top:334px">Salad</h2>
  <p class="menu-card__text dish-line" style="top:384px">Grilled Watermelon &amp; Fig Salad</p>
  <p class="menu-card__text dish-line" style="top:417px">Gem Lettuces, Watermelon, Figs, Toasted Hazelnuts,</p>
  <p class="menu-card__text dish-line" style="top:450px">Balsamic Reduction, Honey-Orange Dressing</p>

  <h2 class="menu-card__text course-heading" style="top:487px">Entrée</h2>

  <svg class="entree-icon" style="left:558px;top:536px" width="70" height="60" viewBox="0 0 70 60">
    <rect role="img" aria-label="Cow silhouette" x="0" y="0" width="70" height="60" rx="10" fill="var(--ink)" opacity="0.85"/>
  </svg>
  <p class="menu-card__text dish-line" style="top:600px">Beef&nbsp; Roasted Filet Mignon, Wild Mushrooms,</p>
  <p class="menu-card__text dish-line" style="top:633px">Garlic Mashed Potatoes, Asparagus with Red Wine Sauce</p>

  <svg class="entree-icon" style="left:562px;top:672px" width="66" height="46" viewBox="0 0 66 46">
    <ellipse role="img" aria-label="Fish silhouette" cx="33" cy="23" rx="33" ry="22" fill="var(--ink)" opacity="0.85"/>
  </svg>
  <p class="menu-card__text dish-line" style="top:728px">Porcini Crusted Halibut, Lemon-Herb Potatoes,</p>
  <p class="menu-card__text dish-line" style="top:760px">Black Kale, Early Girl Tomatoes</p>

  <svg class="entree-icon" style="left:567px;top:785px" width="50" height="68" viewBox="0 0 50 68">
    <rect role="img" aria-label="Carrot silhouette" x="0" y="0" width="50" height="68" rx="12" fill="var(--ink)" opacity="0.85"/>
  </svg>
  <p class="menu-card__text dish-line" style="top:857px">Artichoke Agnolotti, Wild Mushrooms,</p>
  <p class="menu-card__text dish-line" style="top:890px">Baby Arugula, Goat Cheese, White Wine Sauce, Micro herbs</p>

  <h2 class="menu-card__text course-heading course-heading--cake" style="top:925px">Wedding Cake</h2>
  <p class="menu-card__text dish-line" style="top:976px">Delicate Butter Pecan With Fresh Raspberry Mouse</p>
</main>
</body>
</html>
```